Business card Pfotenweide

Business card is for a self-employed dog trainer with own dog school. Name and logo of the dog school are available. Color specifications as well. The design should be classy and minimalist, but also modern. An already existing idea would be: Front: Only the logo Back: Contact data

Font styles to use
Serif
Sans Serif
Other font styles liked:
• Trajan Pro

Colors
f78f20

Requirements
Must have
• Name: Marlene Kessel-Brand Title: Dipl. Dog Trainer Contain my logo Follow my font and color preferences (see files)

```html
<!DOCTYPE html>
<html lang="de">
<head>
<meta charset="utf-8">
<title>Pfotenweide – Visitenkarte</title>
<link rel="stylesheet" href="https://fonts.googleapis.com/css2?family=Cinzel:wght@400;500&family=Marcellus+SC&display=swap">
<style>
  :root {
    --bg: #e9e6e2;
    --brand-brown: #7a6657;
    --brand-brown-dark: #5e4e42;
    --card-white: #ffffff;
    --ink: #2f2a27;
    --rule: #8a7668;
    --shadow: rgba(40, 30, 20, 0.18);
  }
  * { box-sizing: border-box; margin: 0; padding: 0; }
  html, body {
    width: 1200px;
    height: 900px;
    overflow: hidden;
    background: var(--bg);
  }
  .canvas {
    width: 1200px;
    height: 900px;
    display: flex;
    align-items: center;
    justify-content: center;
    gap: 48px;
  }
  .card {
    width: 540px;
    height: 340px;
    border-radius: 4px;
    box-shadow: 0 10px 28px var(--shadow);
    position: relative;
  }

  /* Contact side */
  .card--contact {
    background: var(--card-white);
    padding: 52px 56px 0;
    color: var(--ink);
    text-align: center;
  }
  .contact__name {
    font-family: "Cinzel", serif;
    font-weight: 500;
    font-size: 31px;
    letter-spacing: 0.5px;
    color: var(--brand-brown);
    line-height: 1.1;
  }
  .contact__title {
    font-family: "Marcellus SC", serif;
    font-size: 16px;
    letter-spacing: 0.6px;
    color: var(--brand-brown);
    margin-top: 6px;
  }
  .contact__rule {
    width: 380px;
    height: 1px;
    background: var(--rule);
    margin: 22px auto 24px;
  }
  .contact__line {
    font-family: "Marcellus SC", serif;
    font-size: 16px;
    letter-spacing: 0.5px;
    line-height: 1.9;
    display: flex;
    justify-content: center;
    align-items: center;
    gap: 8px;
  }
  .contact__item {
    display: inline-flex;
    align-items: center;
    gap: 6px;
  }
  .icon {
    width: 13px;
    height: 13px;
    fill: var(--brand-brown);
  }
  .contact__gap { width: 14px; }

  /* Brand side */
  .card--brand {
    background: var(--brand-brown);
    display: flex;
    align-items: center;
    justify-content: center;
  }
  .brand {
    display: flex;
    align-items: center;
    gap: 18px;
    color: var(--card-white);
  }
  .brand__dot {
    width: 104px;
    height: 104px;
    border-radius: 50%;
    background: var(--card-white);
    flex: none;
  }
  .brand__text { display: flex; flex-direction: column; }
  .brand__name {
    font-family: "Cinzel", serif;
    font-weight: 400;
    font-size: 38px;
    letter-spacing: 1px;
    line-height: 1;
  }
  .brand__url {
    font-family: "Cinzel", serif;
    font-size: 11px;
    letter-spacing: 4.4px;
    margin-top: 6px;
  }
</style>
</head>
<body>
<main class="canvas">
  <section class="card card--contact" aria-label="Kontaktseite">
    <h1 class="contact__name">Marlene Kessel-Brand</h1>
    <p class="contact__title">Dipl. Hundetrainerin</p>
    <div class="contact__rule"></div>
    <p class="contact__line">Lindenweg 14, CH-8004 Zürich</p>
    <p class="contact__line">
      <span class="contact__item">
        <svg class="icon" viewBox="0 0 16 16" aria-hidden="true"><path d="M3.6 1.5l2.3 0 1 3.4-1.6 1.3c.9 1.9 2.4 3.4 4.3 4.3l1.3-1.6 3.4 1v2.3c0 .8-.7 1.5-1.5 1.4C7.2 13.3 2.7 8.8 2.2 3c-.1-.8.6-1.5 1.4-1.5z"/></svg>
        079 555 01 20
      </span>
      <span class="contact__gap"></span>
      <span class="contact__item">
        <svg class="icon" viewBox="0 0 16 16" aria-hidden="true"><path d="M5 1h6a1 1 0 0 1 1 1v12a1 1 0 0 1-1 1H5a1 1 0 0 1-1-1V2a1 1 0 0 1 1-1zm.6 1.6v9h4.8v-9zM8 12.6a.8.8 0 1 0 0 1.6.8.8 0 0 0 0-1.6z"/></svg>
        079 555 01 48
      </span>
    </p>
    <p class="contact__line">
      <span class="contact__item">
        <svg class="icon" viewBox="0 0 16 16" aria-hidden="true"><path d="M1 3.5h14v9H1zm1.4 1.2L8 8.8l5.6-4.1z"/></svg>
        info@pfotenweide.com
      </span>
      <span class="contact__gap"></span>
      <span class="contact__item">
        <svg class="icon" viewBox="0 0 16 16" aria-hidden="true"><circle cx="8" cy="8" r="6.5"/></svg>
        www.pfotenweide.com
      </span>
    </p>
  </section>

  <section class="card card--brand" aria-label="Vorderseite">
    <div class="brand">
      <div class="brand__dot"></div>
      <div class="brand__text">
        <span class="brand__name">PFOTENWEIDE</span>
        <span class="brand__url">WWW.PFOTENWEIDE.CH</span>
      </div>
    </div>
  </section>
</main>
</body>
</html>
```